Etiketten für Deodorant in fester Form
Zielgruppe
Naturkosmetik
Aufgabenstellung
Dimension of the tube:
The height of the tube’s body is 53mm
The height of the lid is 20mm
The circular of the body is 126mm

```html
<!DOCTYPE html>
<html lang="de">
<head>
<meta charset="utf-8">
<title>Solvane – Deodorant in fester Form, Etikett</title>
<link rel="stylesheet" href="https://fonts.googleapis.com/css2?family=DM+Serif+Text&family=Poppins:wght@500;600;700&display=swap">
<style>
  :root {
    --page: #f3f3f1;
    --terracotta: #d08358;
    --label-white: #ffffff;
    --accent-text: #d9875a;
    --badge-line: #fbe3d4;
    --brand-teal: #5bc2bb;
    --flower-orange: #f08a44;
    --flower-cream: #fde8dc;
    --leaf-green: #7a8d78;
    --cacao-brown: #6b3b22;
  }
  * { box-sizing: border-box; margin: 0; padding: 0; }
  html, body {
    width: 1200px;
    height: 2317px;
    overflow: hidden;
    background: var(--page);
  }
  .label {
    position: absolute;
    left: 90px;
    top: 685px;
    width: 1020px;
    height: 946px;
    background: var(--terracotta);
    box-shadow: 0 10px 24px rgba(0,0,0,0.18);
  }
  .side-art {
    position: absolute;
    border-radius: 40px;
  }
  .side-art--left {
    left: 0;
    top: 170px;
    width: 304px;
    height: 776px;
    border-radius: 0 120px 0 0;
    background: linear-gradient(170deg, var(--flower-orange) 0%, var(--flower-cream) 45%, var(--terracotta) 100%);
    opacity: 0.85;
  }
  .side-art--right {
    left: 718px;
    top: 300px;
    width: 302px;
    height: 646px;
    border-radius: 120px 0 0 0;
    background: linear-gradient(200deg, var(--leaf-green) 0%, var(--flower-orange) 45%, var(--flower-cream) 100%);
    opacity: 0.85;
  }
  .front-panel {
    position: absolute;
    left: 304px;
    top: 0;
    width: 414px;
    height: 946px;
    background: var(--label-white);
  }
  .arc-line {
    position: absolute;
    left: 0;
    top: 0;
    width: 414px;
    height: 200px;
  }
  .arc-line text {
    font-family: 'Poppins', sans-serif;
    font-weight: 600;
    font-size: 17px;
    letter-spacing: 5px;
    fill: var(--accent-text);
  }
  .brand {
    position: absolute;
    left: 0;
    width: 100%;
    top: 225px;
    text-align: center;
    font-family: 'DM Serif Text', serif;
    font-size: 84px;
    line-height: 1;
    color: var(--brand-teal);
  }
  .headline {
    position: absolute;
    left: 0;
    width: 100%;
    top: 470px;
    text-align: center;
    font-family: 'DM Serif Text', serif;
    font-size: 50px;
    line-height: 1.08;
    color: var(--accent-text);
  }
  .ingredient-art {
    position: absolute;
    left: 30px;
    top: 602px;
    width: 354px;
    height: 180px;
    border-radius: 90px;
    background: radial-gradient(ellipse at center, var(--cacao-brown) 0%, #8a5a3a 40%, #7ea86a 75%, rgba(255,255,255,0) 100%);
  }
  .ingredient-note {
    position: absolute;
    left: 0;
    width: 100%;
    top: 812px;
    text-align: center;
    font-family: 'Poppins', sans-serif;
    font-weight: 600;
    font-size: 28px;
    color: var(--accent-text);
  }
  .net-weight {
    position: absolute;
    left: 0;
    width: 100%;
    top: 848px;
    text-align: center;
    font-family: 'Poppins', sans-serif;
    font-weight: 700;
    font-size: 50px;
    color: var(--accent-text);
  }
  .badge {
    position: absolute;
    left: 749px;
    top: 59px;
    width: 218px;
    height: 218px;
    border: 4px solid var(--badge-line);
    border-radius: 50%;
    display: flex;
    flex-direction: column;
    align-items: center;
    justify-content: center;
    color: var(--badge-line);
    font-family: 'Poppins', sans-serif;
    text-align: center;
  }
  .badge__value {
    font-weight: 700;
    font-size: 50px;
    line-height: 1;
    margin-top: -14px;
  }
  .badge__text {
    font-weight: 600;
    font-size: 22px;
    line-height: 1.15;
    margin-top: 6px;
  }
</style>
</head>
<body>
  <section class="label">
    <div class="side-art side-art--left" role="img" aria-label="Illustration: orange Mohnblüten und cremefarbene Lilie mit grünen Blättern"></div>
    <div class="side-art side-art--right" role="img" aria-label="Illustration: orange und cremefarbene Gänseblümchen mit grünen Blättern"></div>

    <div class="badge">
      <span class="badge__value">100%</span>
      <span class="badge__text">naturlich &amp;<br>vegan</span>
    </div>

    <div class="front-panel">
      <svg class="arc-line" viewBox="0 0 414 200" aria-hidden="false">
        <defs>
          <path id="arc-path" d="M 32 165 A 180 180 0 0 1 382 165"/>
        </defs>
        <text><textPath href="#arc-path" startOffset="50%" text-anchor="middle">DEODORANT IN FEST FORM</textPath></text>
      </svg>

      <div class="brand">Solvane</div>

      <h1 class="headline">Naturkosmetik<br>und BIO</h1>

      <div class="ingredient-art" role="img" aria-label="Illustration: aufgeschnittene Kakaofrucht mit Bohnen und grünen Blättern"></div>

      <p class="ingredient-note">MIT CACAO-BUTTER</p>
      <p class="net-weight">50 g</p>
    </div>
  </section>
</body>
</html>
```